Chocolate company needing sticker for products

I have a small chocolate company Brook Lane Sweets in Austin Texas. I make all vegan, gluten free, organic, faire trade chocolate that tastes amazing! It is allergy friendly approvable by all ages. I want to have a great sticker that i can put on our boxes and bags. I am using a lot of natural craft color and brown. I am open to color options possibly for different flavors. I want the packaging to reflect the basis of my company. It is all handmade by me but i don't want it to have to much of a crafty look to it. I have attached the logo designs I have. it the sticker can have som of the bullet points about the company that would be great. But it needs to say Locally Made in Austin Texas. it also has to have the company address.
417 West Harlow Pine Rd #238 Austin Tx 78719. These things are required by the state for food regulations. I want something that looks great and I can be really proud to put on my product! Thanks so much for all of your help in advance. Dee

I also need some other information added to the sticker. Website which is brooklanesweetsqvz.com 

Phone number 512.555.0187. Instagram brooklanesweets. Thanks for your hard work! 

Industry/Entity Type

Chocolate Company

Requirements
Must have
• The logo is added at the bottom as well as designs I like I want to have a professional look but it to be approvable by all consumers. I will gig feed back as i see what designs come through. This will probably fold out into a multi design project so i will be looking for assistance on other areas of this as well. Thanks

```html
<!DOCTYPE html>
<html lang="en">
<head>
<meta charset="utf-8">
<title>Brook Lane Sweets – Product Stickers</title>
<link rel="stylesheet" href="https://fonts.googleapis.com/css2?family=Cormorant+Garamond:wght@700&family=Source+Sans+3:wght@400;600&display=swap">
<style>
  :root {
    --kraft: #c7a47e;
    --ink: #0c0c0c;
    --paper: #ffffff;
    --marigold: #f5b41d;
    --plum: #5d4486;
  }
  * { margin: 0; padding: 0; box-sizing: border-box; }
  html, body { width: 1200px; height: 840px; overflow: hidden; }
  body { background: var(--kraft); position: relative; }

  .sticker-shapes { position: absolute; left: 0; top: 0; width: 1200px; height: 840px; }

  .label {
    position: absolute;
    width: 200px;
    text-align: center;
    color: var(--paper);
  }
  .label--on-white { color: var(--plum); }

  .ornament {
    display: block;
    width: 22px;
    height: 16px;
    margin: 0 auto;
    background: currentColor;
    border-radius: 2px;
    opacity: .9;
  }
  .ornament--ink { background: var(--plum); }

  .locally-made {
    margin-top: 14px;
    font-family: "Cormorant Garamond", serif;
    font-weight: 700;
    font-size: 11.5px;
    line-height: 1;
  }
  .address {
    font-family: "Source Sans 3", sans-serif;
    font-size: 6px;
    line-height: 1.3;
    letter-spacing: .1px;
  }
  .dotted-rule {
    width: 118px;
    margin: 3px auto 4px;
    border-top: 2px dotted currentColor;
  }
  .brand-name {
    font-family: "Cormorant Garamond", serif;
    font-weight: 700;
    font-size: 30px;
    line-height: 40px;
    text-transform: uppercase;
    letter-spacing: .5px;
  }
  .label--on-white .brand-name { color: var(--ink); }

  .contact {
    margin-top: 6px;
    font-family: "Source Sans 3", sans-serif;
    font-size: 10px;
    line-height: 12px;
  }
  .contact li { list-style: none; display: flex; align-items: center; justify-content: center; gap: 3px; }
  .contact li:first-child { display: block; }
  .contact svg { width: 8px; height: 8px; flex: none; }
  .handle-square {
    width: 7px; height: 7px; flex: none;
    background: currentColor; border-radius: 1px;
  }
  .label .ornament--bottom { margin-top: 8px; }
</style>
</head>
<body>

<svg class="sticker-shapes" viewBox="0 0 1200 840" aria-hidden="true">
  <!-- black sticker -->
  <polygon fill="var(--ink)"
    points="196,247 232,247 368,385 228,523 90,385 90,352 124,352 124,318 158,318 158,283 196,283"/>
  <!-- marigold sticker -->
  <polygon fill="var(--marigold)" points="590,212 765,386 590,560 415,386"/>
  <polygon fill="var(--ink)"
    points="555,248 590,248 728,386 590,524 450,386 450,352 485,352 485,318 520,318 520,283 555,283"/>
  <!-- plum sticker -->
  <polygon fill="var(--plum)" points="998,212 1173,386 998,560 823,386"/>
  <polygon fill="var(--paper)"
    points="963,249 998,249 1135,386 998,524 858,386 858,352 893,352 893,318 928,318 928,283 963,283"/>
</svg>

<!-- Sticker 1: black -->
<div class="label" style="left:130px; top:281px;">
  <span class="ornament" role="img" aria-label="Small decorative flourish"></span>
  <p class="locally-made">Locally Made in Austin Texas</p>
  <p class="address">417 West Harlow Pine Rd #238 Austin Tx 78719</p>
  <div class="dotted-rule"></div>
  <h2 class="brand-name">Brook Lane<br>Sweets</h2>
  <div class="dotted-rule"></div>
  <ul class="contact">
    <li>brooklanesweetsqvz.com</li>
    <li><svg viewBox="0 0 10 10"><path fill="currentColor" d="M2 0.5l2 2-1 1.2c.6 1.3 1.6 2.3 2.8 2.8L7 5.5l2 2-1.2 1.8C4.5 9 1 5.5.7 2.2z"/></svg>512.555.0187</li>
    <li><span class="handle-square"></span>brooklanesweets</li>
  </ul>
  <span class="ornament ornament--bottom" role="img" aria-label="Small decorative flourish"></span>
</div>

<!-- Sticker 2: marigold border -->
<div class="label" style="left:490px; top:282px;">
  <span class="ornament" role="img" aria-label="Small decorative flourish"></span>
  <p class="locally-made">Locally Made in Austin Texas</p>
  <p class="address">417 West Harlow Pine Rd #238 Austin Tx 78719</p>
  <div class="dotted-rule"></div>
  <h2 class="brand-name">Brook Lane<br>Sweets</h2>
  <div class="dotted-rule"></div>
  <ul class="contact">
    <li>brooklanesweetsqvz.com</li>
    <li><svg viewBox="0 0 10 10"><path fill="currentColor" d="M2 0.5l2 2-1 1.2c.6 1.3 1.6 2.3 2.8 2.8L7 5.5l2 2-1.2 1.8C4.5 9 1 5.5.7 2.2z"/></svg>512.555.0187</li>
    <li><span class="handle-square"></span>brooklanesweets</li>
  </ul>
  <span class="ornament ornament--bottom" role="img" aria-label="Small decorative flourish"></span>
</div>

<!-- Sticker 3: plum border, white face -->
<div class="label label--on-white" style="left:898px; top:286px;">
  <span class="ornament ornament--ink" role="img" aria-label="Small decorative flourish"></span>
  <p class="locally-made">Locally Made in Austin Texas</p>
  <p class="address">417 West Harlow Pine Rd #238 Austin Tx 78719</p>
  <div class="dotted-rule" style="border-color:var(--ink)"></div>
  <h2 class="brand-name">Brook Lane<br>Sweets</h2>
  <div class="dotted-rule" style="border-color:var(--ink)"></div>
  <ul class="contact">
    <li>brooklanesweetsqvz.com</li>
    <li><svg viewBox="0 0 10 10"><path fill="currentColor" d="M2 0.5l2 2-1 1.2c.6 1.3 1.6 2.3 2.8 2.8L7 5.5l2 2-1.2 1.8C4.5 9 1 5.5.7 2.2z"/></svg>512.555.0187</li>
    <li><span class="handle-square"></span>brooklanesweets</li>
  </ul>
  <span class="ornament ornament--ink ornament--bottom" role="img" aria-label="Small decorative flourish"></span>
</div>

</body>
</html>
```